Looking for a professional, clean and crisp business card

I am in the underground utilities industry and am just looking for a really impressive business card. I would like our card to be white with our symbol crisp and clear with it protruding. I also have a business partner that will require his name and info on the card once the design is set. I would like to have our website info on the card which is;
http://granitetrenchco.example/

Contact Information for Business Card

Website, contact name, number and email

```html
<!DOCTYPE html>
<html lang="en">
<head>
<meta charset="utf-8">
<title>Granite Trench Co — Business Card</title>
<link rel="stylesheet" href="https://fonts.googleapis.com/css2?family=Lato:wght@400;700;900&display=swap">
<style>
  :root {
    --ink: #2b2b2b;
    --night: #151617;
    --paper: #ffffff;
    --brand-blue: #2f6db5;
    --rule: #3a3a3a;
    --edge: #9a9a9a;
    --canvas: #ffffff;
  }
  * { box-sizing: border-box; margin: 0; padding: 0; }
  html, body {
    width: 1045px;
    height: 1200px;
    overflow: hidden;
    background: var(--canvas);
    font-family: "Lato", Arial, sans-serif;
  }
  .card {
    position: absolute;
    left: 0;
    width: 1045px;
    height: 588px;
  }
  .card--front {
    top: 0;
    background: var(--night);
    border: 1px solid #444;
  }
  .card--back {
    top: 611px;
    background: var(--paper);
    border: 1.5px solid var(--edge);
  }
  .front-wordmark {
    position: absolute;
    left: 0;
    width: 100%;
    top: 215px;
    text-align: center;
    color: var(--paper);
    font-weight: 900;
    font-size: 58px;
    letter-spacing: 1px;
  }
  .front-website {
    position: absolute;
    left: 0;
    width: 100%;
    top: 487px;
    text-align: center;
    color: var(--brand-blue);
    font-size: 34px;
    font-weight: 400;
  }
  .back-wordmark {
    position: absolute;
    left: 110px;
    width 220px;
    width: 220px;
    top: 224px;
    text-align: center;
    color: var(--ink);
    font-weight: 900;
    font-size: 34px;
    line-height: 1.2;
  }
  .divider {
    position: absolute;
    left: 371px;
    top: 158px;
    width: 2px;
    height: 272px;
    background: var(--rule);
  }
  .contact {
    position: absolute;
    left: 424px;
    top: 174px;
    color: var(--ink);
  }
  .contact__name {
    font-weight: 700;
    font-size: 38px;
    margin-bottom: 14px;
  }
  .contact__list { list-style: none; }
  .contact__item {
    display: flex;
    align-items: center;
    height: 52px;
    font-size: 34px;
    font-weight: 400;
  }
  .contact__icon {
    width: 28px;
    height: 28px;
    margin-right: 26px;
    flex: none;
  }
</style>
</head>
<body>
  <section class="card card--front">
    <div class="front-wordmark">Granite Trench Co</div>
    <div class="front-website">www.granitetrenchco.example</div>
  </section>

  <section class="card card--back">
    <div class="back-wordmark">Granite Trench Co</div>
    <div class="divider"></div>
    <div class="contact">
      <p class="contact__name">Person Name</p>
      <ul class="contact__list">
        <li class="contact__item">
          <svg class="contact__icon" viewBox="0 0 28 28" aria-hidden="true">
            <rect x="7" y="2" width="14" height="24" rx="3" fill="none" stroke="var(--brand-blue)" stroke-width="3"/>
            <rect x="8" y="19" width="12" height="6" fill="var(--brand-blue)"/>
          </svg>
          <span>555-014-2378</span>
        </li>
        <li class="contact__item">
          <svg class="contact__icon" viewBox="0 0 28 28" aria-hidden="true">
            <rect x="1" y="6" width="26" height="17" rx="1.5" fill="var(--brand-blue)"/>
            <path d="M2 7 L14 16 L26 7" fill="none" stroke="var(--paper)" stroke-width="2"/>
            <path d="M2 22 L11 14 M26 22 L17 14" fill="none" stroke="var(--paper)" stroke-width="1.5"/>
          </svg>
          <span>info@granitetrenchco.example</span>
        </li>
        <li class="contact__item">
          <svg class="contact__icon" viewBox="0 0 28 28" aria-hidden="true">
            <circle cx="14" cy="14" r="12" fill="var(--brand-blue)"/>
            <g fill="none" stroke="var(--paper)" stroke-width="1.6">
              <ellipse cx="14" cy="14" rx="5" ry="12"/>
              <line x1="2" y1="14" x2="26" y2="14"/>
              <line x1="14" y1="2" x2="14" y2="26"/>
              <path d="M4 8 H24 M4 20 H24"/>
            </g>
          </svg>
          <span>www.granitetrenchco.example</span>
        </li>
      </ul>
    </div>
  </section>
</body>
</html>
```